Plakat-Design für kleines IT Systemhaus
Zielgruppe
Wir sind ein kleines IT Systemhaus. Unser Bereich für das Plakat ist Virtual Datacenter/ IAAS also Cloud server und oder IT Support
Aufgabenstellung
Die Werbefläche steht an einer viel befahrenen Strasse und ist gut sichtbar. Die masse sind: 2760 x 1280 mm das design kann für vorder- und Rückseite entworfen werden. wichtig ist. das Ganze einfach, klar sichtbar und Kontaktmotivierend zu gestallten. Da an der Strasse also nicht zu voll mit Text.

```html
<!DOCTYPE html>
<html lang="de">
<head>
<meta charset="utf-8">
<title>KORVAN – Plakat</title>
<link href="https://fonts.googleapis.com/css2?family=Montserrat:wght@800&family=Cabin:wght@500&display=swap" rel="stylesheet">
<style>
  :root {
    --page-bg: #e0e0e0;
    --banner-dark: #1f1f21;
    --teal: #1f9a96;
    --teal-dark: #0f6f6b;
    --white: #f4f4f4;
    --photo-warm: #6f6a63;
    --photo-cool: #3b4a5e;
  }
  html, body {
    margin: 0;
    width: 1200px;
    height: 864px;
    overflow: hidden;
    background: var(--page-bg);
  }
  .banner {
    position: absolute;
    left: 20px;
    top: 151px;
    width: 1160px;
    height: 562px;
    background: var(--banner-dark);
    overflow: hidden;
  }
  .banner__photo {
    position: absolute;
    left: 0;
    top: 0;
    width: 640px;
    height: 100%;
    background:
      linear-gradient(90deg, rgba(31,31,33,0) 45%, var(--banner-dark) 100%),
      linear-gradient(160deg, var(--photo-warm) 0%, #4a4d52 35%, var(--photo-cool) 60%, #2a2c30 100%);
  }
  .brand {
    position: absolute;
    right: 32px;
    top: 70px;
    font-family: "Montserrat", sans-serif;
    font-weight: 800;
    font-size: 46px;
    letter-spacing: 2px;
    color: var(--white);
    line-height: 1;
  }
  .headline {
    position: absolute;
    right: 31px;
    top: 170px;
    margin: 0;
    text-align: right;
    font-family: "Montserrat", sans-serif;
    font-weight: 800;
    font-size: 44px;
    line-height: 57px;
    color: var(--white);
    white-space: nowrap;
  }
  .headline__accent { color: var(--teal); }
  .services {
    position: absolute;
    top: 373px;
    left: 325px;
    right: 32px;
    display: flex;
    gap: 19px;
    margin: 0;
    padding: 0;
    list-style: none;
  }
  .services__item {
    height: 54px;
    display: flex;
    align-items: center;
    justify-content: center;
    background: linear-gradient(180deg, var(--teal) 0%, var(--teal-dark) 100%);
    color: var(--white);
    font-family: "Cabin", sans-serif;
    font-weight: 500;
    font-size: 29px;
  }
  .services__item--datacenter { width: 366px; }
  .services__item--cloud { width: 199px; }
  .services__item--support { flex: 1; }
  .contact {
    position: absolute;
    top: 468px;
    left: 323px;
    margin: 0;
    font-family: "Cabin", sans-serif;
    font-weight: 500;
    font-size: 28px;
    color: var(--white);
    white-space: nowrap;
  }
</style>
</head>
<body>
  <section class="banner">
    <div class="banner__photo" role="img" aria-label="Foto: IT-Techniker mit Laptop vor Serverschränken in einem Rechenzentrum"></div>
    <div class="brand">KORVAN</div>
    <h1 class="headline">
      <span class="headline__accent">WIR UNTERSTÜTZEN KMU UND</span><br>
      <span class="headline__accent">EINZELFIRMEN,</span> LANGFRISTIG<br>
      UND BEDARFSORIENTIERT
    </h1>
    <ul class="services">
      <li class="services__item services__item--datacenter">Virtuelles Rechenzentrum</li>
      <li class="services__item services__item--cloud">Cloud-Server</li>
      <li class="services__item services__item--support">IT-Support</li>
    </ul>
    <p class="contact">Lindenrain 14 | 6072 Sachseln | +41 41 555 01 23 | www.korvan.ch</p>
  </section>
</body>
</html>
```